Business Card Design

We have our logo and everything in place. Looking to have a layout for our new business cards designed. These will be printed with a matte finish, possibly rounded corners, and looking to incorporate some cool spot UV layers into the design.

Ive uploaded the existing card front and back as well as our logo.

Card Size Will Be 3.5" x 2"

```html
<!DOCTYPE html>
<html lang="en">
<head>
<meta charset="utf-8">
<title>Timberline Deck and Rail – Business Card</title>
<link rel="stylesheet" href="https://fonts.googleapis.com/css2?family=Libre+Baskerville:ital,wght@0,400;0,700;1,400&display=swap">
<style>
  :root {
    --backdrop: #5b5b5d;
    --card: #141415;
    --card-gloss: #2e2e31;
    --card-mid: #1d1d1f;
    --ink: #f4f4f4;
    --accent: #2c8fd6;
    --rule: #8a8a8a;
  }
  * { box-sizing: border-box; margin: 0; padding: 0; }
  html, body { width: 1200px; height: 787px; overflow: hidden; }
  body {
    background: var(--backdrop);
    font-family: "Libre Baskerville", Georgia, serif;
    position: relative;
  }
  .card {
    position: absolute;
    top: 243px;
    width: 525px;
    height: 300px;
    border-radius: 22px;
    background: var(--card);
    overflow: hidden;
    box-shadow: 0 10px 24px rgba(0,0,0,0.35);
  }
  .card--back { left: 50px; }
  .card--front { left: 625px; }
  /* Spot UV gloss layer: soft sheen standing in for the chevron varnish pattern */
  .spot-uv-field {
    position: absolute;
    inset: 0;
    background: linear-gradient(120deg,
      var(--card) 0%,
      var(--card-mid) 22%,
      var(--card-gloss) 40%,
      var(--card-mid) 58%,
      var(--card-gloss) 76%,
      var(--card) 100%);
  }
  .brand {
    position: absolute;
    left: 44px;
    top: 32px;
    width: 270px;
    text-align: center;
    color: var(--ink);
  }
  .brand__name {
    font-size: 44px;
    font-weight: 400;
    line-height: 1.05;
  }
  .brand__tagline {
    margin-top: 6px;
    padding-top: 6px;
    border-top: 1px solid var(--rule);
    font-size: 10px;
    letter-spacing: 3px;
    text-transform: uppercase;
  }
  .person {
    position: absolute;
    left: 44px;
    top: 128px;
    color: var(--ink);
  }
  .person__name {
    font-size: 22px;
    font-weight: 700;
    letter-spacing: 1px;
    text-transform: uppercase;
  }
  .person__title {
    font-size: 14px;
    font-style: italic;
    color: var(--accent);
    margin-top: 2px;
  }
  .contact {
    position: absolute;
    left: 44px;
    top: 192px;
    list-style: none;
    color: var(--ink);
    font-size: 15px;
  }
  .contact__item {
    display: flex;
    align-items: center;
    gap: 10px;
    line-height: 28px;
  }
  .contact__icon { width: 14px; height: 14px; flex: none; fill: var(--ink); }
</style>
</head>
<body>
  <div class="card card--back">
    <div class="spot-uv-field" role="img" aria-label="Gloss spot UV chevron pattern covering the whole matte black card back"></div>
  </div>

  <div class="card card--front">
    <div class="spot-uv-field" role="img" aria-label="Gloss spot UV chevron pattern covering the matte black card front"></div>

    <div class="brand">
      <div class="brand__name">Timberline</div>
      <div class="brand__tagline">Deck and Rail</div>
    </div>

    <div class="person">
      <div class="person__name">Daniel Mercer</div>
      <div class="person__title">President</div>
    </div>

    <ul class="contact">
      <li class="contact__item">
        <svg class="contact__icon" viewBox="0 0 16 16" aria-hidden="true"><path d="M3.6 1.2 6 3.6 4.6 5.6c.9 2.2 3.6 4.9 5.8 5.8l2-1.4 2.4 2.4-1.6 2.2C8 14.4 1.6 8 1.4 2.8z"/></svg>
        <span>403.555.0187</span>
      </li>
      <li class="contact__item">
        <svg class="contact__icon" viewBox="0 0 16 16" aria-hidden="true"><path d="M1 3h14v10H1z M2 4v.6l6 4 6-4V4z" fill-rule="evenodd"/></svg>
        <span>timberlinedeckrail@mail.com</span>
      </li>
      <li class="contact__item">
        <svg class="contact__icon" viewBox="0 0 16 16" aria-hidden="true"><circle cx="8" cy="8" r="7"/><path d="M1 8h14M8 1c-2.5 3-2.5 11 0 14M8 1c2.5 3 2.5 11 0 14" stroke="#141415" stroke-width="1.1" fill="none"/></svg>
        <span>www.timberlinedeckrail.com</span>
      </li>
    </ul>
  </div>
</body>
</html>
```